Accounting Practice Business Card Design

I have a logo I am happy for you to use in the design of the Business Card.
You can edit and change colours as you please, I am not fixated on it.
I am looking for a modern and clean overall feel for the finished design.

The business is a small accounting practice who thrives on word of mouth referrals and this card will be given to all current and prospect clients.

Industry/Entity Type

Accountant

Contact Information for Business Card

Marcus Elwin
Level 5, 8 Corvale Ridge Road
ASHGROVE RISE VIC 3187
Phone: 9481 3057
Email: melwin@mrfaccountants.com.au
Web: www.mrfaccountants.com.au

Font styles to use
Serif
Sans Serif

Colors
0555a3
3277b5
85acd3
0393ce
33a6d7
85cae6
00a990
33b8a4
9bcb3c

Requirements
Must have
• "The end to your tax problems begin with us"
• "A referral from you is our greatest compliment"
Nice to have
• Modern clean professional

```html
<!DOCTYPE html>
<html lang="en">
<head>
<meta charset="utf-8">
<title>MRF Accountants – Business Card</title>
<link rel="stylesheet" href="https://fonts.googleapis.com/css2?family=Roboto+Condensed:wght@400;700&family=Merriweather:ital,wght@1,400&display=swap">
<style>
  :root {
    --stage: #0a4a58;
    --card-navy: #084a68;
    --facet-line: #1f86c4;
    --ink: #3a6480;
    --rule: #1d5b6e;
    --band: #0a6470;
    --white: #ffffff;
    --soft-blue: #85cae6;
    --green: #9bcb3c;
    --teal: #00a990;
  }
  html, body {
    margin: 0;
    width: 1200px;
    height: 820px;
    overflow: hidden;
    background: var(--stage);
  }
  .canvas { position: relative; width: 1200px; height: 820px; }
  .card { position: absolute; top: 256px; width: 490px; height: 275px; overflow: hidden; background: var(--card-navy); }
  .card svg { position: absolute; inset: 0; display: block; }
  .card-front { left: 91px; }
  .card-back { left: 615px; }

  .wordmark {
    position: absolute;
    font-family: "Roboto Condensed", sans-serif;
    font-weight: 700;
    color: var(--white);
    text-align: center;
    line-height: 1;
    letter-spacing: 1px;
  }
  .card-front .wordmark { left: 0; right: 0; top: 82px; font-size: 62px; }
  .card-front .wordmark span { display: block; font-size: 28px; margin-top: 6px; letter-spacing: 1px; }
  .card-back .wordmark { left: 372px; width: 112px; top: 124px; font-size: 30px; }
  .card-back .wordmark span { display: block; font-size: 13px; margin-top: 3px; }

  .tagline {
    position: absolute; left: 0; right: 0; margin: 0;
    font-family: "Merriweather", serif; font-style: italic; font-weight: 400;
    text-align: center; line-height: 1;
  }
  .card-front .tagline { top: 200px; font-size: 12px; color: var(--soft-blue); letter-spacing: .3px; }
  .card-back .tagline { top: 259px; left: 0; width: 300px; font-size: 8px; color: var(--ink); }

  .holder-name {
    position: absolute; left: 55px; top: 47px;
    font-family: "Roboto Condensed", sans-serif; font-weight: 700;
    font-size: 29px; letter-spacing: 1.5px; color: var(--ink);
    text-transform: uppercase; margin: 0; line-height: 1;
  }
  .contact {
    position: absolute; left: 62px;
    font-family: "Roboto Condensed", sans-serif; font-size: 9.5px;
    letter-spacing: .6px; color: var(--rule); text-transform: uppercase;
    line-height: 10px; margin: 0;
  }
  .contact-phone { top: 113px; }
  .contact-address { top: 156px; }
  .web {
    position: absolute; left: 0; right: 0; top: 214px;
    font-family: "Roboto Condensed", sans-serif; font-weight: 700;
    font-size: 21px; letter-spacing: 1.5px; color: var(--white);
    text-align: center; text-transform: uppercase; line-height: 30px;
  }
</style>
</head>
<body>
<main class="canvas">

  <section class="card card-front" aria-label="Card front">
    <svg viewBox="0 0 490 275" aria-hidden="true">
      <g stroke="var(--facet-line)" stroke-width="1" fill="none" opacity=".8">
        <line x1="0" y1="40" x2="60" y2="0"/>
        <line x1="0" y1="90" x2="110" y2="0"/>
        <line x1="380" y1="275" x2="490" y2="195"/>
        <line x1="430" y1="275" x2="490" y2="235"/>
      </g>
    </svg>
    <div class="wordmark">MRF<span>ACCOUNTANTS</span></div>
    <p class="tagline">The end to your tax problems begin with us</p>
  </section>

  <section class="card card-back" aria-label="Card back">
    <svg viewBox="0 0 490 275" aria-hidden="true">
      <g stroke="var(--facet-line)" stroke-width="1" fill="none" opacity=".8">
        <line x1="400" y1="0" x2="490" y2="55"/>
        <line x1="440" y1="275" x2="490" y2="240"/>
      </g>
      <path d="M0 0 H316 Q424 138 316 275 H0 Z" fill="var(--teal)"/>
      <path d="M0 0 H309 Q416 138 309 275 H0 Z" fill="var(--green)"/>
      <path d="M0 0 H300 Q410 138 300 275 H0 Z" fill="var(--white)"/>
      <line x1="0" y1="35" x2="324" y2="35" stroke="var(--rule)" stroke-width="2"/>
      <line x1="0" y1="91" x2="346" y2="91" stroke="var(--rule)" stroke-width="2"/>
      <g fill="var(--rule)">
        <rect x="30" y="115" width="20" height="14"/>
        <path d="M30 115 L40 123 L50 115" stroke="var(--white)" stroke-width="1.4" fill="none"/>
        <path d="M26 167 L40 155 L54 167 L50 167 L50 180 L30 180 L30 167 Z"/>
        <rect x="37" y="171" width="6" height="9" fill="var(--white)"/>
      </g>
      <rect x="0" y="205" width="490" height="49" fill="var(--band)"/>
    </svg>
    <h1 class="holder-name">Marcus Elwin</h1>
    <p class="contact contact-phone">Phone: 9481 3057<br>Email: melwin@mrfaccountants.com.au</p>
    <p class="contact contact-address">Level 5, 8 Corvale Ridge Road<br>Ashgrove Rise VIC 3187</p>
    <div class="wordmark">MRF<span>ACCOUNTANTS</span></div>
    <div class="web">www.mrfaccountants.com.au</div>
    <p class="tagline">A referral from you is our greatest compliment</p>
  </section>

</main>
</body>
</html>
```